Business Card Design

Contact Information for Business Card

A vertical business card request- a medium & light gray with silverfern tree logo (logo is attached)

Please use Trebuchet font -- if possible- can we use two different color gray? (See pictures attached below)
Info on the front should be the Silverfern tree logo - on the top of the card, followed by the info ...
Card to read: " " indicated what should be on the card --
Name: " Joan Pelley "
Title : "Partner "
" Office: 202.555.0147 "
" Mobile: 202.555.0182 "

Backside of the card - solid medium color gray color w/ address and small message centered in the card - Trebuchet font
to read:

" 317 B North Linden Avenue, NE "
" Washington, DC 20099 "

Then below address to read:
" Fundraising | Event Planning | Political Consulting "

```html
<!DOCTYPE html>
<html lang="en">
<head>
<meta charset="utf-8">
<title>Silverfern Strategies – Business Cards</title>
<link rel="stylesheet" href="https://fonts.googleapis.com/css2?family=PT+Sans:wght@400;700&display=swap">
<style>
  :root {
    --page-bg: #eceeee;
    --gray-medium: #58595b;
    --gray-light: #c9cacc;
    --ink-dark: #4a4b4d;
    --ink-light: #e6e7e8;
    --white: #ffffff;
    --card-shadow: 0 18px 40px rgba(0, 0, 0, 0.18);
  }
  * { box-sizing: border-box; margin: 0; padding: 0; }
  html, body {
    width: 1200px;
    height: 1039px;
    overflow: hidden;
    background: var(--page-bg);
    font-family: "Trebuchet MS", "PT Sans", sans-serif;
  }
  .card-sheet {
    width: 1200px;
    height: 1039px;
    display: flex;
    align-items: center;
    justify-content: center;
    gap: 90px;
  }
  .card {
    width: 330px;
    height: 576px;
    box-shadow: var(--card-shadow);
    position: relative;
    overflow: hidden;
  }

  /* Front */
  .card-front { background: var(--gray-light); }
  .front-band {
    position: absolute;
    left: 0; top: 0;
    width: 100%;
    height: 248px;
    background: var(--gray-medium);
  }
  .band-notch {
    position: absolute;
    left: 46px;
    top: 247px;
    width: 44px;
    height: 18px;
  }
  .brand {
    position: absolute;
    right: 30px;
    top: 118px;
    text-align: right;
    color: var(--white);
    font-weight: 400;
    line-height: 1;
  }
  .brand-name {
    display: block;
    font-size: 36px;
    letter-spacing: 1px;
  }
  .brand-sub {
    display: block;
    font-size: 15px;
    letter-spacing: 2px;
    margin-top: 6px;
  }
  .front-details {
    position: absolute;
    left: 36px;
    top: 298px;
    color: var(--ink-dark);
  }
  .person-name { font-size: 30px; font-weight: 400; line-height: 1.1; }
  .person-title { font-size: 11px; margin-top: 4px; }
  .person-email { font-size: 14px; margin-top: 22px; }
  .phone-list { list-style: none; margin-top: 26px; font-size: 17px; line-height: 1.45; }

  /* Back */
  .card-back {
    background: var(--gray-medium);
    display: flex;
    flex-direction: column;
    align-items: center;
    justify-content: center;
    color: var(--ink-light);
    text-align: center;
  }
  .address { font-style: normal; font-size: 15px; line-height: 1.5; }
  .services { font-size: 11px; margin-top: 22px; letter-spacing: 0.2px; }
</style>
</head>
<body>
  <main class="card-sheet">
    <article class="card card-front" aria-label="Business card front">
      <div class="front-band"></div>
      <svg class="band-notch" viewBox="0 0 44 18" aria-hidden="true">
        <polygon points="0,0 44,0 22,18" fill="var(--gray-medium)"/>
      </svg>
      <h1 class="brand">
        <span class="brand-name">SILVERFERN</span>
        <span class="brand-sub">STRATEGIES</span>
      </h1>
      <section class="front-details">
        <h2 class="person-name">Joan Pelley</h2>
        <p class="person-title">Partner</p>
        <p class="person-email">joan@silverfernllc.com</p>
        <ul class="phone-list">
          <li>Office: 202.555.0147</li>
          <li>Mobile: 202.555.0182</li>
        </ul>
      </section>
    </article>

    <article class="card card-back" aria-label="Business card back">
      <address class="address">
        317 B North Linden Avenue, NE<br>
        Suit A<br>
        Washington, DC 20099
      </address>
      <p class="services">Fundraising | Event Planning | Political Consulting</p>
    </article>
  </main>
</body>
</html>
```